International Food Manufacturer in the need of a new business card and logo.

Our Company - Northgate Pantry Ltd.

Our Industry - Food and Drink

We are a Wild Harvested Food Distributor / Manufacturer. We service the following food sectors: Supermarkets, Hotels, Restaurants, Cafes, Catering and all people looking to eat healthy food products.

Slogan - Pure wild harvest for every healthy kitchen

Business card details -

48-52 Marlow Lane
Hatherby Green
London
EC9Z 4RT United Kingdom
Dennis Prowle
+44 7000 481736 - UK
+971 50 7739205 - UAE
+38 063 914 2758 - Ukraine
dennis@northgatepantry.example
www.northgatepantry.example

Goal - We are looking for a dynamic modern new look for our corporate image and a designer who can bring this new concept to our future food product designs. Please try to incorporate 3d hexagonal vector Imaging in your design concepts.

Target Market(s)

Industry/Entity Type

Food Service

Contact Information for Business Card

Northgate Pantry Ltd.
48-52 Marlow Lane
Hatherby Green
London
EC9Z 4RT United Kingdom
Dennis Prowle
+44 7000 481736 - UK
+971 50 7739205 - UAE

Font styles to use
Serif

Colors

Designer to choose colors to be used in the design.

Requirements
Must have
• Please read project description above.
Nice to have
Should not have

```html
<!DOCTYPE html>
<html lang="en">
<head>
<meta charset="utf-8">
<title>Northgate Pantry Ltd. — Logo and Visiting Card</title>
<link rel="stylesheet" href="https://fonts.googleapis.com/css2?family=EB+Garamond:wght@400;600&family=Inter:wght@400&display=swap">
<style>
  :root {
    --navy: #33447a;
    --green: #8dc54a;
    --label-grey: #c9c9c9;
    --paper: #ffffff;
    --canvas: #ffffff;
  }
  * { margin: 0; padding: 0; box-sizing: border-box; }
  html, body {
    width: 1200px; height: 1000px; overflow: hidden;
    background: var(--canvas);
  }
  .board { position: relative; width: 1200px; height: 1000px; }

  .section-label {
    position: absolute; left: 90px;
    font-family: "Inter", "Helvetica Neue", Arial, sans-serif;
    font-size: 20px; color: var(--label-grey); letter-spacing: 0.3px;
  }
  .section-label--logo { top: 60px; }
  .section-label--card { top: 330px; }

  /* Logo lockup */
  .lockup { position: absolute; display: flex; align-items: center; }
  .lockup__dot { border-radius: 50%; background: var(--navy); flex: none; }
  .lockup__text { display: flex; flex-direction: column; }
  .lockup__name {
    font-family: "EB Garamond", Garamond, Georgia, serif;
    font-weight: 400; color: var(--navy);
    text-transform: uppercase; white-space: nowrap;
  }
  .lockup__name-line { display: block; }
  .lockup__tagline {
    font-family: "EB Garamond", Garamond, Georgia, serif;
    font-weight: 600; color: var(--navy);
    text-transform: uppercase; white-space: nowrap;
  }

  .lockup--main { left: 330px; top: 145px; gap: 16px; }
  .lockup--main .lockup__dot { width: 108px; height: 108px; }
  .lockup--main .lockup__name { font-size: 50px; line-height: 0.92; letter-spacing: 3.5px; }
  .lockup--main .lockup__tagline { font-size: 11.5px; letter-spacing: 1.1px; margin-top: 8px; }

  /* Visiting card */
  .card {
    position: absolute; left: 174px; top: 391px;
    width: 852px; height: 470px;
    background: var(--paper); overflow: hidden;
    box-shadow: 0 0 22px rgba(0,0,0,0.10);
  }
  .lockup--card { left: 34px; top: 34px; gap: 9px; }
  .lockup--card .lockup__dot { width: 70px; height: 70px; }
  .lockup--card .lockup__name { font-size: 31px; line-height: 0.92; letter-spacing: 2px; }
  .lockup--card .lockup__tagline { font-size: 7.2px; letter-spacing: 0.6px; margin-top: 5px; }

  .contact {
    position: absolute; left: 33px; top: 161px;
    font-family: "EB Garamond", Garamond, Georgia, serif;
    color: var(--navy); font-size: 18px; line-height: 30.5px;
  }
  .contact__name {
    color: var(--green); font-size: 23px; letter-spacing: 0.5px;
    text-transform: uppercase; line-height: 30px;
  }
  .contact__address { margin-top: 10px; }

  .card__artwork {
    position: absolute; left: 516px; top: 0;
    width: 336px; height: 470px;
    background: linear-gradient(160deg, var(--navy) 0%, var(--navy) 45%, var(--green) 100%);
  }
</style>
</head>
<body>
<main class="board">
  <p class="section-label section-label--logo">Logo Deisgn</p>

  <div class="lockup lockup--main">
    <span class="lockup__dot" aria-hidden="true"></span>
    <div class="lockup__text">
      <span class="lockup__name">
        <span class="lockup__name-line">Northgate</span>
        <span class="lockup__name-line">Pantry Ltd.</span>
      </span>
      <span class="lockup__tagline">Pure wild harvest for every healthy kitchen</span>
    </div>
  </div>

  <p class="section-label section-label--card">Visiting card</p>

  <section class="card">
    <div class="lockup lockup--card">
      <span class="lockup__dot" aria-hidden="true"></span>
      <div class="lockup__text">
        <span class="lockup__name">
          <span class="lockup__name-line">Northgate</span>
          <span class="lockup__name-line">Pantry Ltd.</span>
        </span>
        <span class="lockup__tagline">Pure wild harvest for every healthy kitchen</span>
      </div>
    </div>

    <div class="contact">
      <p class="contact__name">Dennis Prowle</p>
      <p>+44 7000 481736 – UK</p>
      <p>+971 50 7739205 – UAE</p>
      <p>+38 063 914 2758 – Ukraine</p>
      <div class="contact__address">
        <p>48–52 Marlow Lane</p>
        <p>Hatherby Green, London</p>
        <p>EC9Z 4RT United Kingdom</p>
        <p>E: dennis@northgatepantry.example</p>
        <p>W: www.northgatepantry.example</p>
      </div>
    </div>

    <div class="card__artwork" role="img" aria-label="Large brand emblem artwork in navy and leaf green"></div>
  </section>
</main>
</body>
</html>
```